Web design for Marketplace

Guys!
1st of all, thank you for willing to help me out.
I have attached PDF file with examples.
I am looking for professional and clean design for my new project “ Lantern of Seers “. Its marketplace for Psychic Readers around the world. Where they will able to register to provide their services via Chat,Email and sell their products on their personal stores.
Customer will able to get services and buy products from Psychic on Marketplace.
url : http://www.lanternofseers-demo.net
Please note: it doesn’t matter, what my current site looks like. I am looking for completely new design.
It doesn't matter if you add or remove : Clipvale video or even text which is on the home page in new design.
Following are the main pages of the website, which i am looking to be design.
1. Home page
2. Psychic
3. Marketplace
4. Psychic profile page
5. Psychic Store page
6. Psychic product page
7. Logo
following is the website, which i like the most. I would love to have something like that. It is neat , clean and friendly. I am looking for depth in design and neatness and borders (matter and a lot and it should be prefect ).
http://www.craftnook-demo.net
P.S : i believe it will be helpful to choose one of you. If you can only create design of " Homepage" at 1st , so i can go ahead and hire one of you guys.
Best,
Hi guys!
Guys,

```html
<!DOCTYPE html>
<html lang="en">
<head>
<meta charset="utf-8">
<title>Lantern of Seers — Home</title>
<link href="https://fonts.googleapis.com/css2?family=Raleway:wght@400;500;700;800&family=Open+Sans:wght@400;600&display=swap" rel="stylesheet">
<style>
:root{
  --orange:#f26522;
  --orange-dark:#d94f10;
  --nav:#5c5c5c;
  --nav-dark:#4a4a4a;
  --panel:#e6dfe3;
  --panel-edge:#d8d0d5;
  --text:#555;
  --muted:#888;
  --line:#e4e4e4;
  --star:#f7941d;
  --footer:#ddd5da;
}
*{margin:0;padding:0;box-sizing:border-box}
html,body{width:986px;height:1200px;overflow:hidden}
body{position:relative;background:#fff;font-family:Arial,Helvetica,sans-serif;color:var(--text)}
.abs{position:absolute}
.header-band{left:0;top:0;width:986px;height:157px;background:linear-gradient(#fff,#ece7ea)}
.logo{left:75px;top:18px;color:#222}
.logo-name{font-family:'Raleway',sans-serif;font-weight:800;font-size:26px;color:#222;display:flex;align-items:center;gap:7px}
.logo-name i{display:inline-block;width:12px;height:12px;border-radius:50%;background:var(--orange)}
.logo-tag{font-family:'Open Sans',sans-serif;font-size:15px;color:#333;margin-top:3px}
.top-links{right:72px;top:28px;font-size:11px;color:var(--orange)}
.top-links span{margin:0 6px;color:var(--orange)}
.cart{right:105px;top:51px;text-align:right;font-size:10px;color:#777;line-height:14px}
.cart b{font-weight:normal;font-size:12px;color:#666}
.cart svg{position:absolute;left:-36px;top:2px}
.page{left:74px;top:105px;width:839px;height:1000px;background:#fff;border:1px solid #eee}
.nav{left:77px;top:108px;width:832px;height:49px;background:linear-gradient(#6a6a6a,#505050);display:flex}
.nav a{color:#fff;font-size:11px;text-decoration:none;display:flex;align-items:center;justify-content:center;border-right:1px solid #444;height:100%;white-space:nowrap}
.nav a.active{background:linear-gradient(#fb8448,var(--orange))}
.search{position:absolute;left:628px;top:10px;width:195px;height:24px;background:#fff;border:1px solid #ccc;font-size:10px;color:#333;padding:6px 16px}
.search svg{position:absolute;right:8px;top:5px}
.hero{left:79px;top:159px;width:829px;height:279px;border:3px solid #ddd;background:linear-gradient(90deg,#f3f1f2,#fff 60%,#f6f6f6)}
.hero-photo{position:absolute;right:3px;top:12px;width:370px;height:258px;background:radial-gradient(ellipse at 70% 55%,#d9342b 0,#c8433a 25%,#e7cfc4 45%,#f7f3f2 70%);border-radius:4px}
.hero h1{position:absolute;left:48px;top:38px;font-family:'Raleway',sans-serif;font-weight:400;font-size:20px;color:var(--orange);letter-spacing:.3px}
.hero p{position:absolute;left:48px;top:77px;width:352px;font-size:11px;line-height:19px;color:#666;text-align:justify}
.cta{position:absolute;left:48px;top:180px;width:351px;height:48px;background:#e8e4e6;display:flex;align-items:center;padding-left:24px}
.cta span{font-family:'Raleway',sans-serif;font-size:19px;color:#666;letter-spacing:.5px}
.btn{background:linear-gradient(#fb7a3a,var(--orange-dark));color:#fff;font-family:'Raleway',sans-serif;font-weight:800;border-radius:3px;border:1px solid #d2460b;display:inline-flex;align-items:center;justify-content:center}
.join{margin-left:20px;width:119px;height:27px;font-size:12px;gap:10px}
.join i{width:14px;height:14px;border-radius:50%;background:#fff;color:var(--orange);font-style:normal;font-size:10px;display:flex;align-items:center;justify-content:center}
.hero-arrows{position:absolute;left:49px;top:241px;display:flex;gap:1px}
.hero-arrows i{width:16px;height:18px;background:#8a8a8a;display:flex;align-items:center;justify-content:center;color:#fff;font-style:normal;font-size:11px}
.hero-arrows i:first-child{border-radius:9px 0 0 9px}
.hero-arrows i:last-child{border-radius:0 9px 9px 0}
.side-box{left:81px;width:213px;background:var(--panel);border:1px solid var(--panel-edge)}
.side-box .inner{position:absolute;left:4px;right:4px;bottom:4px;background:#fff}
.side-title{font-family:'Raleway',sans-serif;font-size:16px;color:#333;position:absolute}
.video{top:451px;height:162px;padding:4px}
.video-still{width:100%;height:100%;background:linear-gradient(90deg,#2e2c2b,#7c6b5d 45%,#3a3632 75%,#222);position:relative}
.video-still .play{position:absolute;left:83px;top:62px;width:40px;height:34px;background:#ddd;border-radius:5px;border:2px solid #fff}
.video-still .play:after{content:"";position:absolute;left:14px;top:8px;border-left:13px solid #444;border-top:8px solid transparent;border-bottom:8px solid transparent}
.video-still .cap{position:absolute;left:30px;bottom:10px;color:#eee;font-family:'Raleway',sans-serif;font-weight:700;font-size:13px}
.market{top:619px;height:174px}
.market .inner{top:38px}
.prod{position:absolute;top:10px;width:71px;height:108px;border:1px solid #ddd;text-align:center;font-size:9px;color:#333}
.prod .ph{width:52px;height:68px;margin:4px auto 0}
.prod em{display:block;font-style:normal;color:var(--orange);font-size:10px;margin-top:6px}
.news{top:799px;height:131px}
.news .inner{top:38px}
.news input{position:absolute;left:15px;top:12px;width:174px;height:32px;border:1px solid #ccc;font-size:9px;padding-left:17px;color:#555;font-family:Arial,sans-serif}
.subscribe{position:absolute;left:123px;top:50px;width:84px;height:27px;font-size:11px}
.readers-title{left:305px;top:449px;font-family:'Raleway',sans-serif;font-weight:400;font-size:18px;color:var(--orange)}
.round-arrow{width:15px;height:15px;border-radius:50%;background:#aaa;color:#fff;font-size:10px;display:flex;align-items:center;justify-content:center}
.card{width:290px;height:131px;border:1px solid var(--line);box-shadow:0 1px 3px rgba(0,0,0,.08);background:#fff}
.card .avatar{position:absolute;left:16px;top:16px;width:100px;height:100px;border-radius:50%;border:5px solid #eee}
.card .divider{position:absolute;left:127px;top:10px;bottom:10px;width:1px;background:var(--line)}
.card h3{position:absolute;left:141px;top:12px;font-family:'Open Sans',sans-serif;font-weight:400;font-size:14.5px;color:var(--orange)}
.card .price{position:absolute;left:141px;top:35px;font-size:9px;color:#555}
.card .price b{color:var(--star);font-weight:normal;font-size:12px;letter-spacing:-1px;margin-left:4px}
.card p{position:absolute;left:141px;top:57px;width:134px;font-size:10.3px;line-height:15.5px;color:#999;text-align:justify}
.card p a{color:var(--orange);text-decoration:none}
.products{left:81px;top:936px;width:821px;height:158px;background:var(--panel);border:1px solid var(--panel-edge)}
.products h2{position:absolute;left:21px;top:9px;font-family:'Raleway',sans-serif;font-weight:400;font-size:18px;color:#333}
.products .arrows{position:absolute;right:22px;top:10px;font-size:14px;color:#555;letter-spacing:4px}
.products .inner{position:absolute;left:4px;top:38px;right:4px;bottom:4px;background:#fff}
.thumb{position:absolute;top:13px;width:89px;height:89px;border:1px solid #ddd;padding:4px}
.thumb div{width:100%;height:100%}
.footer{left:0;top:1116px;width:986px;height:84px;background:var(--footer)}
.footer nav{position:absolute;left:74px;top:20px;font-size:11px;color:#444}
.footer nav span{margin:0 8px;color:#666}
.footer .copy{position:absolute;left:74px;top:47px;font-size:11px;color:#444}
.social{position:absolute;right:74px;top:30px;display:flex;gap:8px}
.social i{width:20px;height:20px;border-radius:50%;background:#aaa}
</style>
</head>
<body>
<div class="abs header-band"></div>
<div class="abs logo">
  <div class="logo-name"><i></i>Lantern of Seers</div>
  <div class="logo-tag">a world of psychics</div>
</div>
<div class="abs top-links">HELP<span>|</span>LOGIN<span>|</span>SIGNUP</div>
<div class="abs cart">
  <svg width="22" height="20" viewBox="0 0 22 20" fill="none" stroke="#777" stroke-width="1.5"><path d="M1 2h4l3 11h10l2-8H6"/><circle cx="9" cy="17" r="1.5"/><circle cx="17" cy="17" r="1.5"/></svg>
  MY CART - (0) ITEMS<br><b>$00.00</b>
</div>

<div class="abs page"></div>
<nav class="abs nav">
  <a class="active" style="width:62px">HOME</a><a style="width:75px">PSYCHIC</a><a style="width:108px">MARKETPLACE</a><a style="width:125px">PSYCHIC PROFILE</a><a style="width:116px">PSYCHIC STORE</a><a style="width:129px">PSYCHIC PRODUCT</a>
  <div class="search">Search
    <svg width="14" height="14" viewBox="0 0 14 14"><circle cx="5.5" cy="5.5" r="4" fill="none" stroke="#222" stroke-width="2"/><path d="M8.5 8.5l4 4" stroke="#222" stroke-width="2.5"/></svg>
  </div>
</nav>

<section class="abs hero">
  <div class="hero-photo" role="img" aria-label="Young man in a red t-shirt typing on a laptop"></div>
  <h1>WELCOME TO LOS</h1>
  <p>If you have an issue in your life that is causing you any sort of distress, no matter what it is, a reading from one of our psychics will give you immediate, compassionate insight. There are moments when you need more answers than you can get on your own. That's why the gifted psychics at Lantern of Seers are here for you, 24/7.</p>
  <div class="cta"><span>ARE YOU PSYCHIC?</span><a class="btn join">JOIN NOW <i>&#8250;</i></a></div>
  <div class="hero-arrows"><i>&#8249;</i><i>&#8250;</i></div>
</section>

<aside class="abs side-box video">
  <div class="video-still" role="img" aria-label="Clipvale video still of a woman speaking">
    <div class="play"></div>
    <div class="cap">Can you be psychic?</div>
  </div>
</aside>
<aside class="abs side-box market">
  <div class="side-title" style="left:36px;top:9px">Psychic Marketplace</div>
  <div class="inner">
    <div class="prod" style="left:19px"><div class="ph" role="img" aria-label="Red heart love spell artwork" style="background:radial-gradient(circle,#b0162a,#2a0508)"></div><em>Love Spell</em>$200.00</div>
    <div class="prod" style="left:130px"><div class="ph" role="img" aria-label="Lit white candle with roses" style="background:radial-gradient(circle at 50% 40%,#f4e6d0,#5a1a2a 50%,#140a10)"></div><em>Love Spell</em>$200.00</div>
  </div>
</aside>
<aside class="abs side-box news">
  <svg class="abs" style="left:10px;top:5px" width="30" height="28" viewBox="0 0 30 28"><rect x="1" y="5" width="28" height="20" fill="#f7f7f7" stroke="#ccc"/><path d="M1 5l14 11 14-11" fill="none" stroke="#ccc"/></svg>
  <div class="side-title" style="left:46px;top:9px">Newsletter Subscribe</div>
  <div class="inner">
    <input type="text" value="Enter your mail ID">
    <a class="btn subscribe">SUBSCRIBE</a>
  </div>
</aside>

<h2 class="abs readers-title">TOP PSYCHIC READERS</h2>
<div class="abs round-arrow" style="left:881px;top:451px">&#8250;</div>

<article class="abs card" style="left:308px;top:482px"><div class="avatar" role="img" aria-label="Portrait photo of psychic reader" style="background:radial-gradient(circle,#b47a55,#5a3020)"></div><div class="divider"></div><h3>Aron Velde</h3><div class="price">$5.00/ Min &nbsp;:: <b>★★★★☆</b></div><p>Morbi pulvinar erat et libero facilisis sit amet vestibulum blandit bibendum non at turpis romate. <a>more...</a></p></article>
<article class="abs card" style="left:615px;top:482px"><div class="avatar" role="img" aria-label="Portrait photo of psychic reader" style="background:radial-gradient(circle,#6f8a5a,#23331c)"></div><div class="divider"></div><h3>Aron Velde</h3><div class="price">$5.00/ Min &nbsp;:: <b>★★★★☆</b></div><p>Morbi pulvinar erat et libero facilisis sit amet vestibulum blandit bibendum non at turpis romate. <a>more...</a></p></article>
<article class="abs card" style="left:308px;top:627px"><div class="avatar" role="img" aria-label="Portrait photo of psychic reader" style="background:radial-gradient(circle,#d7b4a0,#eee)"></div><div class="divider"></div><h3>Aron Velde</h3><div class="price">$5.00/ Min &nbsp;:: <b>★★★★☆</b></div><p>Morbi pulvinar erat et libero facilisis sit amet vestibulum blandit bibendum non at turpis romate. <a>more...</a></p></article>
<article class="abs card" style="left:615px;top:627px"><div class="avatar" role="img" aria-label="Portrait photo of psychic reader" style="background:radial-gradient(circle,#e6c5b0,#fff)"></div><div class="divider"></div><h3>Aron Velde</h3><div class="price">$5.00/ Min &nbsp;:: <b>★★★★☆</b></div><p>Morbi pulvinar erat et libero facilisis sit amet vestibulum blandit bibendum non at turpis romate. <a>more...</a></p></article>
<article class="abs card" style="left:308px;top:774px"><div class="avatar" role="img" aria-label="Portrait photo of psychic reader" style="background:radial-gradient(circle,#e3c1a6,#fafafa)"></div><div class="divider"></div><h3>Aron Velde</h3><div class="price">$5.00/ Min &nbsp;:: <b>★★★★☆</b></div><p>Morbi pulvinar erat et libero facilisis sit amet vestibulum blandit bibendum non at turpis romate. <a>more...</a></p></article>
<article class="abs card" style="left:615px;top:774px"><div class="avatar" role="img" aria-label="Portrait photo of psychic reader" style="background:radial-gradient(circle,#c27a55,#3a1a10)"></div><div class="divider"></div><h3>Aron Velde</h3><div class="price">$5.00/ Min &nbsp;:: <b>★★★★☆</b></div><p>Morbi pulvinar erat et libero facilisis sit amet vestibulum blandit bibendum non at turpis romate. <a>more...</a></p></article>

<section class="abs products">
  <h2>Our Products</h2>
  <div class="arrows">&lsaquo;&rsaquo;</div>
  <div class="inner">
    <div class="thumb" style="left:19px"><div role="img" aria-label="Teal scarf with anchor pendant" style="background:linear-gradient(135deg,#3aa0b0,#2f6b2a)"></div></div>
    <div class="thumb" style="left:118px"><div role="img" aria-label="Engraved business sign" style="background:linear-gradient(#ddd,#bbb)"></div></div>
    <div class="thumb" style="left:217px"><div role="img" aria-label="Wedding couple with name sign" style="background:linear-gradient(90deg,#1e2433,#e8e8ec)"></div></div>
    <div class="thumb" style="left:316px"><div role="img" aria-label="Framed lettering sign" style="background:linear-gradient(#222,#777,#222)"></div></div>
    <div class="thumb" style="left:415px"><div role="img" aria-label="Printed turquoise shirt" style="background:linear-gradient(#4cb8c8,#2a8ea0)"></div></div>
    <div class="thumb" style="left:514px"><div role="img" aria-label="Beaded bracelet" style="background:radial-gradient(circle,#b46a3a,#f4f0ee 60%)"></div></div>
    <div class="thumb" style="left:613px"><div role="img" aria-label="Jewelled hair comb on black" style="background:linear-gradient(#111,#aaa 50%,#111)"></div></div>
    <div class="thumb" style="left:712px"><div role="img" aria-label="Pale blue evening gown" style="background:linear-gradient(90deg,#c8b49a,#d8dde2,#c8b49a)"></div></div>
  </div>
</section>

<footer class="abs footer">
  <nav>Home<span>|</span>Psychic<span>|</span>Marketplace<span>|</span>Psychic profile<span>|</span>Psychic Store<span>|</span>Psychic product<span>|</span>Sign in<span>|</span>Register</nav>
  <div class="copy">Copyright &copy; 2013 www.lanternofseers-demo.net &nbsp;&nbsp; All rights reserved.</div>
  <div class="social"><i></i><i></i><i></i><i></i></div>
</footer>
</body>
</html>
```